Electrician Needs A Business Card

I already have a logo and would like a business card to be designed based around this logo the company is called Coralwood Electrical Pty Ltd

The business card will be printed on transparent plastic so I need it to stand out from the crowd. I do not want the card to have anything to do with Electrical on it eg light bulbs, power points etc

I need it to have the following details.

Dominic Farrow
Mobile : 0452 317 908
email : dominic@coralwoodelectrical.com.au

If it could incorporate the following onto the bottom of the card
ELECTRICAL - COMMUNICATIONS - AUDIO - VISUAL

```html
<!DOCTYPE html>
<html lang="en">
<head>
<meta charset="utf-8">
<title>Coralwood Electrical – Business Card</title>
<link rel="stylesheet" href="https://fonts.googleapis.com/css2?family=Arimo:wght@400;700&display=swap">
<style>
  :root {
    --page: #ffffff;
    --ink: #3a3a3a;
    --ink-dark: #2b2b2b;
    --accent: #f5a62b;
    --frame: #3d3d3d;
  }
  html, body {
    margin: 0;
    padding: 0;
    width: 1200px;
    height: 1000px;
    overflow: hidden;
    background: var(--page);
  }
  .canvas {
    position: relative;
    width: 1200px;
    height: 1000px;
    font-family: "Arimo", Arial, sans-serif;
  }
  .card {
    position: absolute;
    left: 80px;
    top: 157px;
    width: 1036px;
    height: 682px;
    border: 2px solid var(--frame);
    background: var(--page);
  }
  .brand {
    position: absolute;
    left: 0;
    right: 0;
    top: 160px;
    display: flex;
    justify-content: center;
    align-items: center;
    gap: 16px;
  }
  .brand-mark {
    width: 30px;
    height: 30px;
    background: var(--accent);
  }
  .brand-name {
    font-weight: 700;
    font-size: 40px;
    color: var(--ink-dark);
    letter-spacing: 1px;
  }
  .person-name {
    position: absolute;
    left: 0;
    right: 0;
    top: 394px;
    margin: 0;
    text-align: center;
    font-weight: 700;
    font-size: 34px;
    letter-spacing: 2.5px;
    color: var(--ink);
  }
  .contact {
    position: absolute;
    left: 0;
    right: 0;
    top: 440px;
    margin: 0;
    text-align: center;
    font-size: 26px;
    color: var(--ink);
  }
  .services {
    position: absolute;
    left: 0;
    right: 0;
    top: 590px;
    margin: 0;
    text-align: center;
    font-size: 36px;
    color: var(--ink-dark);
    letter-spacing: 0.3px;
  }
  .services .highlight { color: var(--accent); }
</style>
</head>
<body>
<div class="canvas">
  <div class="card">
    <div class="brand">
      <span class="brand-mark"></span>
      <span class="brand-name">Coralwood Electrical</span>
    </div>
    <h1 class="person-name">Dominic Farrow</h1>
    <p class="contact">(M) : 0452 317 908 (E) : dominic@coralwoodelectrical.com.au</p>
    <p class="services"><span class="highlight">ELECTRICAL</span> - COMMUNICATIONS - <span class="highlight">AUDIO</span> - VISUAL</p>
  </div>
</div>
</body>
</html>
```